Buch-/E-Book-Cover für Buch über die Ausdrucksweise
Zielgruppe
Deutsche Version
Ich bin Autor und habe ich Buch über 'Ausdrucksweise verbessern' geschrieben. Das Buch steht aktuell zum Verkauf. Allerdings gefällt mir das Cover nicht gut. Deswegen möchte ich gerne ein neues Cover erstellen lassen. Der Haupttitel lautet 'Klarheit gewinnt immer' und der Untertitel: 'Ausdrucksweise verbessern & Wortschatz erweitern: Der Praxisguide mit konkreten Beispielen, wie Sie in jedem Gespräch mit Rhetorik und Sprachkompetenz' Autor ist 'Jonas Brettler'
English Version
I am an author and I have written a book on 'Improving Expression'. The book is currently for sale. However, I don't like the cover very much. Therefore, I would like to have a new cover created. The main title is 'Clarity always wins the day = Klarheit gewinnt immer' and the subtitle is: 'Improve expression & expand vocabulary: The practical guide with concrete examples of how you can use rhetoric and language skills in every conversation' = 'Ausdrucksweise verbessern & Wortschatz erweitern: Der Praxisguide mit konkreten Beispielen, wie Sie in jedem Gespräch mit Rhetorik und Sprachkompetenz'. Author is 'Jonas Brettler'.
Aufgabenstellung
Ich habe das aktuelle Cover beigefügt. Mir gefällt die Symbolik des aktuellen Covers noch nicht. Ich denke mit dem Titel 'Klarheit gewinnt immer' kann man noch mehr herausholen, indem man eine bessere Symbolik verwendet. Wichtig ist, dass der potenzielle Kunde sofort die Symbolik mit dem Inhalt assoziiert.
Die Konkurrenzbücher auf Bookvanta können gute Hinweise sein. Allerdings sollte das neue Cover hier explizit herausstechen: https://www.bookvanta-shop.de/s?k=redekunst+lernen&i=titel&sprefix=redek%2Ctitel%2C12&ref=nv_sr_qq_lm-kx-a_1_10
Folgende Punkte sind wichtig:
- Haupttitel muss gut lesbar sein. (Untertitel ist unwichtig)
- 'Praxisguide' sollte herausstechen
- Es sollte erkenntlich gemacht werden, dass das Buch ein Hörbuch enthält
Ich habe die Covervorlage mit dem passendem Format hinzugefügt.
English Version:
I have attached the current cover. I don't like the symbolism of the current cover yet. I think with the title 'Clarity always wins the day' you can get more out of it by using better symbolism. It is important that the potential customer immediately associates the symbolism with the content.
Competitor books on Bookvanta can be good clues. However, the new cover should explicitly stand out here: https://www.bookvanta-shop.de/s?k=redekunst+learn&i=titel&sprefix=speechcr%2Ctitel%2C12&ref=nv_sr_qq_lm-kx-a_1_10
The following points are important:
- Main title must be easy to read. (Subtitle is not important).
- The cover and the title must be recognizable even in very small format (thumb size - see bookvanta)
- 'Praxisguide should stand out
- It should be made recognizable that the book contains an audio book 'Inkl.Hörbuch'
I have added the cover template with the appropriate format.

```html
<!DOCTYPE html>
<html lang="de">
<head>
<meta charset="utf-8">
<title>Klarheit gewinnt immer – Buchcover</title>
<link rel="stylesheet" href="https://fonts.googleapis.com/css2?family=Roboto:wght@700;900&family=Roboto+Condensed:wght@400;700&display=swap">
<style>
  :root {
    --board-light: #5b6070;
    --board-mid: #464b5a;
    --board-dark: #2b2f3c;
    --title-red: #a60417;
    --title-yellow: #f2c136;
    --badge-orange: #e8552e;
    --headphone-yellow: #d9d12a;
    --badge-text: #ffffff;
    --shirt-blue: #8fa3bd;
    --skin-tone: #c79a84;
    --sweater-gold: #d8a32a;
  }
  * { margin: 0; padding: 0; box-sizing: border-box; }
  html, body { width: 750px; height: 1200px; overflow: hidden; background: var(--board-dark); }
  .cover {
    position: relative;
    width: 750px;
    height: 1200px;
    overflow: hidden;
    font-family: "Roboto Condensed", "Arial Narrow", sans-serif;
  }
  .cover__backdrop {
    position: absolute; inset: 0;
    background: radial-gradient(ellipse at 48% 38%, var(--board-light) 0%, var(--board-mid) 45%, var(--board-dark) 100%);
  }
  .cover__person { position: absolute; }
  .cover__person--left {
    left: 0; top: 655px; width: 240px; height: 545px;
    background: linear-gradient(180deg, rgba(199,154,132,0.55) 0%, rgba(143,163,189,0.75) 35%, var(--shirt-blue) 100%);
    border-radius: 0 110px 0 0;
  }
  .cover__person--right {
    left: 640px; top: 700px; width: 110px; height: 500px;
    background: linear-gradient(180deg, rgba(199,154,132,0.55) 0%, rgba(216,163,42,0.8) 35%, var(--sweater-gold) 100%);
    border-radius: 90px 0 0 0;
  }
  .audio-badge {
    position: absolute; left: 450px; top: 14px; width: 240px; height: 240px;
  }
  .audio-badge__headphones {
    position: absolute; inset: 0;
    border-radius: 50%;
    background: radial-gradient(circle closest-side, transparent 62%, rgba(217,209,42,0.6) 74%, transparent 100%);
  }
  .audio-badge__circle {
    position: absolute; left: 41px; top: 59px; width: 158px; height: 158px;
    border-radius: 50%;
    background: var(--badge-orange);
    color: var(--badge-text);
    display: flex; flex-direction: column; align-items: center; justify-content: center;
    font-weight: 700;
    line-height: 1;
  }
  .audio-badge__small { font-size: 21px; margin-top: -4px; }
  .audio-badge__large { font-size: 39px; margin-top: 4px; }
  .title {
    position: absolute; left: 0; width: 750px; text-align: center;
    text-transform: uppercase;
  }
  .title__line { display: block; line-height: 1; }
  .title__line--first {
    position: absolute; left: 0; width: 750px; top: 236px;
    font-family: "Roboto", Arial, sans-serif; font-weight: 900;
    font-size: 126px; color: var(--title-red); letter-spacing: -1px;
    padding-right: 22px;
  }
  .title__line--link {
    position: absolute; left: 0; width: 750px; top: 348px;
    font-weight: 700;
    font-size: 50px; color: var(--title-yellow);
    padding-right: 20px;
  }
  .title__line--last {
    position: absolute; left: 0; width: 750px; top: 400px;
    font-family: "Roboto", Arial, sans-serif; font-weight: 900;
    font-size: 126px; color: var(--title-yellow); letter-spacing: -1px;
    padding-right: 14px;
  }
  .subtitle {
    position: absolute; left: 170px; width: 436px; top: 720px;
    text-align: center; color: var(--title-yellow);
  }
  .subtitle__lead { font-size: 19.5px; line-height: 24px; white-space: nowrap; }
  .subtitle__highlight {
    display: block; font-weight: 700; font-size: 53px; line-height: 1;
    color: var(--title-red); margin-top: 6px; letter-spacing: 0.5px;
  }
  .subtitle__body { font-size: 19.5px; line-height: 27px; margin-top: 6px; white-space: nowrap; }
  .author {
    position: absolute; left: 0; width: 770px; top: 1120px;
    text-align: center; color: var(--title-yellow);
    font-weight: 700; font-size: 31px; line-height: 1;
  }
</style>
</head>
<body>
  <main class="cover">
    <div class="cover__backdrop" role="img" aria-label="Dunkle Schiefertafel mit einer großen, mit Kreide gezeichneten Sprechblase"></div>

    <div class="cover__person cover__person--left" role="img" aria-label="Foto eines lachenden Mannes mit Bart im karierten Hemd, der gestikulierend spricht"></div>
    <div class="cover__person cover__person--right" role="img" aria-label="Foto einer lachenden Frau im gelben Pullover, die dem Mann zuhört"></div>

    <div class="audio-badge">
      <div class="audio-badge__headphones" role="img" aria-label="Gelbe Kopfhörer um den Hörbuch-Hinweis"></div>
      <div class="audio-badge__circle">
        <span class="audio-badge__small">inkl.</span>
        <span class="audio-badge__large">Hörbuch</span>
      </div>
    </div>

    <h1 class="title">
      <span class="title__line title__line--first">Klarheit</span>
      <span class="title__line title__line--link">gewinnt</span>
      <span class="title__line title__line--last">immer</span>
    </h1>

    <div class="subtitle">
      <p class="subtitle__lead">Ausdrucksweise verbessern &amp; Wortschatz erweitern:</p>
      <strong class="subtitle__highlight">DER PRAXISGUIDE</strong>
      <p class="subtitle__body">mit konkreten Beispielen, wie Sie in jedem Gespräch<br>mit Rhetorik und Sprachkompetenz überzeugen</p>
    </div>

    <p class="author">Jonas Brettler</p>
  </main>
</body>
</html>
```